Sunshine Valley B.C. Recreational Real Estate Billboard

entrance bill board for each way on the hwy. Vintage
SUNSHINE VALLEY B.C.
Get back to Nature
Lots for sale
Sales office: next right / left with arrow
website fernhollowhomes.com
ownfernhollow.com
phone -1 604 555-0193
our logo please see below

We love the Adirondack chairs looking at mountains illustrated
vintage style

Target Market(s)

people driving past on hwy 3, families, nature lovers, away from city, log cabin, healthy living

Industry/Entity Type

Resort Real Estate /Recreational Real Estate / nature

Font styles to use
Sans Serif
Other font styles liked:
• vintage text

Colors
00AB8E
00BBA5
67D7C9
C6EFE9
E9F9F6
FFC000
F8CF3A
FAE287
FDF2CF
FEFAEE
F0912C
F2A743
F7CA91
FBE8D2
FDF5EE

Requirements
Must have
• vintage resort look, two red Adirondack chairs in a special spot looking out at two mountains meeting at a valley with a lake in front of valley old Zestra Pop art work style, Lake Tahoe, Muskoka look
Nice to have
• trees, mountains, Muskoka/ Adirondack chairs

```html
<!DOCTYPE html>
<html lang="en">
<head>
<meta charset="utf-8">
<title>Fern Hollow – Lots For Sale Billboard</title>
<link rel="stylesheet" href="https://fonts.googleapis.com/css2?family=Josefin+Slab:wght@700&family=Lobster&family=Raleway:wght@400&family=Roboto+Condensed:wght@500&display=swap">
<style>
  :root {
    --panel-orange: #df9a52;
    --panel-orange-deep: #d98f45;
    --brown: #4e2a0c;
    --brown-dark: #3a1f08;
    --ink: #38332e;
    --white: #ffffff;
    --sky-top: #e9b27a;
    --sky-glow: #f7e6c8;
    --sky-low: #e8733a;
    --mountain: #8d7a5c;
    --forest: #5d6a2e;
    --lake: #8fa98f;
    --deck: #c9ad8a;
    --chair-red: #c2452c;
  }
  * { margin: 0; padding: 0; box-sizing: border-box; }
  html, body { width: 1200px; height: 562px; overflow: hidden; background: var(--white); }
  .billboard {
    position: relative;
    width: 1200px;
    height: 562px;
    overflow: hidden;
    font-family: "Josefin Slab", serif;
  }
  .panel {
    position: absolute;
    left: 0; top: 0;
    width: 1072px; height: 562px;
    background: var(--panel-orange);
  }
  .scene {
    position: absolute;
    left: 0; top: 0;
    width: 760px; height: 562px;
    background:
      linear-gradient(90deg, rgba(223,154,82,0) 0%, rgba(223,154,82,0) 78%, var(--panel-orange) 100%),
      radial-gradient(ellipse 120px 90px at 560px 120px, var(--sky-glow) 0%, rgba(247,230,200,0) 100%),
      linear-gradient(180deg,
        var(--sky-top) 0%,
        var(--sky-low) 28%,
        var(--mountain) 40%,
        var(--forest) 50%,
        var(--lake) 58%,
        var(--lake) 70%,
        var(--chair-red) 78%,
        var(--deck) 92%,
        var(--deck) 100%);
  }
  .brand {
    position: absolute;
    left: 770px; top: 62px;
    width: 180px;
    text-align: center;
    color: var(--brown-dark);
    font-family: "Josefin Slab", serif;
    font-weight: 700;
    line-height: 1.1;
  }
  .brand-mark {
    display: block;
    width: 14px; height: 14px;
    margin: 0 auto 6px;
    border-radius: 50%;
    background: var(--brown-dark);
  }
  .brand-name { font-size: 18px; letter-spacing: 0.5px; }
  .brand-sub { font-size: 9px; letter-spacing: 0.8px; }
  .brand-place {
    margin-top: 3px;
    padding-top: 2px;
    border-top: 1px solid var(--brown-dark);
    font-size: 5px;
    letter-spacing: 0.6px;
  }
  .headline {
    position: absolute;
    left: 706px; top: 142px;
    width: 310px;
    color: var(--brown);
    font-family: "Lobster", cursive;
    transform: rotate(-8deg);
    transform-origin: left top;
    line-height: 0.95;
  }
  .headline-top { display: block; font-size: 50px; }
  .headline-main { display: block; font-size: 86px; padding-left: 28px; }
  .offer {
    position: absolute;
    left: 711px; top: 330px;
    color: var(--brown);
    font-size: 40px;
    letter-spacing: 1px;
  }
  .contact {
    position: absolute;
    left: 700px; top: 432px;
    width: 340px;
    text-align: center;
    color: var(--ink);
    font-family: "Josefin Slab", serif;
    font-size: 23px;
    line-height: 33px;
  }
  .contact-phone { font-family: "Roboto Condensed", sans-serif; font-weight: 500; font-size: 22px; }
  .direction-strip {
    position: absolute;
    left: 1072px; top: 0;
    width: 128px; height: 562px;
    background: var(--white);
  }
  .arrow { position: absolute; left: 18px; width: 89px; height: 57px; }
  .arrow-top { top: 23px; }
  .arrow-bottom { top: 480px; }
  .direction-text {
    position: absolute;
    left: 64px; top: 290px;
    transform: translate(-50%, -50%) rotate(-90deg);
    white-space: nowrap;
    font-family: "Raleway", sans-serif;
    font-weight: 400;
    font-size: 38px;
    line-height: 36px;
    color: var(--brown-dark);
    text-align: left;
  }
</style>
</head>
<body>
  <main class="billboard">
    <div class="panel"></div>
    <div class="scene" role="img" aria-label="Vintage painted illustration of two red Adirondack chairs on a wooden dock looking out over a lake toward mountains meeting in a valley at sunset, with evergreen forest on the shore"></div>

    <div class="brand">
      <span class="brand-mark"></span>
      <div class="brand-name">FERN HOLLOW</div>
      <div class="brand-sub">DEVELOPMENTS LTD.</div>
      <div class="brand-place">FERN HOLLOW • BRITISH COLUMBIA</div>
    </div>

    <h1 class="headline">
      <span class="headline-top">Get Back to</span>
      <span class="headline-main">Nature</span>
    </h1>

    <p class="offer">LOTS FOR SALE</p>

    <div class="contact">
      <div>fernhollowhomes.com</div>
      <div>ownfernhollow.com</div>
      <div class="contact-phone">+1 604 555-0193</div>
    </div>

    <aside class="direction-strip">
      <svg class="arrow arrow-top" viewBox="0 0 89 57" aria-hidden="true">
        <polygon points="0,15 50,15 50,0 89,28.5 50,57 50,42 0,42" fill="var(--brown)"/>
      </svg>
      <div class="direction-text">SALES OFFICE:<br>NEXT RIGHT</div>
      <svg class="arrow arrow-bottom" viewBox="0 0 89 57" aria-hidden="true">
        <polygon points="0,15 50,15 50,0 89,28.5 50,57 50,42 0,42" fill="var(--brown)"/>
      </svg>
    </aside>
  </main>
</body>
</html>
```